Business Cards for Demolition & Salvage Company

We are Licensed Demolition Contractors and this business card design is for our Salvage Yard. We recycle over 95% of the building materials removed from each demolition site in which we take to our Salvage Yard for resale eg. bricks, windows, doors, kitchens, stoves, lights, fencing etc so pretty much everything.
Updates

I forgot to note that single sided business card only please.

Reason: I would like to ask if designers could please submit or re-submit their designs edited to a single sided card only. The card also does not need space for an employee name or position as our general business contact details will suffice for this project. Primary colour must be ROYAL BLUE with no exceptions please. Much appreciated and thank you to all whom have submitted designs to date and I look forward to receiving your edited designs..

Industry/Entity Type

Building

Contact Information for Business Card

Tolvanek Demolition & Salvage (WA) Pty Ltd
2317 Carrowby Ridge Road
LOWER MIRRABEL WA 6182
P: (08) 9473 5068
F: (08) 9473 2257
E: salvage@tkwreck.com.au
W: tolvanekdemolition.com.au

Requirements
Must have
• We have a logo that has been with our Company since 1974 so he must be included in the design - file attached. As for colours, we have always used royal blue and again this must be the primary colour used in the design. Please keep the design simple.
Nice to have
• Card can include opening hours as follows:
Opening Hours:
Monday to Friday 8am - 5.00pm
Saturday 8am - 3pm
Closed Sunday's and public holidays

```html
<!DOCTYPE html>
<html lang="en">
<head>
<meta charset="utf-8">
<title>Tolvanek Demolition &amp; Salvage — Business Cards</title>
<link href="https://fonts.googleapis.com/css2?family=EB+Garamond:wght@500;600&display=swap" rel="stylesheet">
<style>
  :root {
    --stage: #8a8d93;
    --card-light: #d5d9d9;
    --card-dark: #060606;
    --royal: #2346c8;
    --royal-bright: #4169e1;
    --navy: #1f2a6b;
    --white: #f4f4f4;
  }
  * { box-sizing: border-box; margin: 0; padding: 0; }
  html, body { width: 1200px; height: 960px; overflow: hidden; }
  body {
    background: var(--stage);
    font-family: "EB Garamond", Georgia, serif;
    display: flex;
    align-items: center;
    justify-content: center;
    gap: 80px;
  }
  .card {
    position: relative;
    width: 440px;
    height: 720px;
    padding: 40px 38px;
    box-shadow: 0 10px 30px rgba(0,0,0,.35);
  }
  .card--light { background: var(--card-light); --text: var(--navy); --accent: var(--royal); --icon-cut: #d5d9d9; }
  .card--dark { background: var(--card-dark); --text: var(--white); --accent: var(--royal-bright); --icon-cut: #060606; }

  .brand-mark {
    display: flex;
    align-items: center;
    gap: 10px;
    margin-left: 120px;
    height: 90px;
  }
  .brand-mark__dot {
    width: 40px; height: 40px;
    border-radius: 50%;
    background: var(--accent);
  }
  .brand-mark__name {
    font-size: 26px;
    font-weight: 600;
    color: var(--accent);
  }
  .company {
    margin-top: 14px;
    text-align: right;
    color: var(--accent);
    font-weight: 600;
    font-size: 27px;
    line-height: 1.15;
  }
  .company span { display: block; }
  .company span:last-child { margin-right: 40px; }

  .contacts {
    list-style: none;
    margin-top: 40px;
    color: var(--text);
    font-size: 21px;
    font-weight: 500;
    line-height: 1.25;
  }
  .contacts li {
    display: flex;
    align-items: flex-start;
    gap: 14px;
    margin-bottom: 6px;
  }
  .contacts svg { flex: none; width: 20px; height: 20px; margin-top: 3px; fill: var(--accent); }
  .contacts .cut { stroke: var(--icon-cut); }

  .hours {
    margin-top: 60px;
    color: var(--text);
    font-size: 20px;
    font-weight: 500;
    line-height: 1.35;
  }
  .hours__title { color: var(--accent); font-size: 23px; font-weight: 600; margin-bottom: 4px; }
  .hours p { padding-left: 14px; }
</style>
</head>
<body>

<article class="card card--light">
  <div class="brand-mark"><span class="brand-mark__dot"></span><span class="brand-mark__name">Tolvanek</span></div>
  <h1 class="company"><span>Tolvanek Demolition</span><span>&amp; Salvage (WA) Pty Ltd</span></h1>
  <ul class="contacts">
    <li><svg viewBox="0 0 20 20"><path d="M10 1a6 6 0 0 0-6 6c0 5 6 12 6 12s6-7 6-12a6 6 0 0 0-6-6z"/></svg><span>2317 Carrowby Ridge Road<br>LOWER MIRRABEL WA 6182</span></li>
    <li><svg viewBox="0 0 20 20"><path d="M5 2l3 4-2 2c1 2 3 4 5 5l2-2 4 3-2 4C8 17 3 12 2 5z"/></svg><span>(08) 9473 5068</span></li>
    <li><svg viewBox="0 0 20 20"><path d="M5 2h8v5H5zM2 8h16v8H2zM5 13h10v5H5z"/></svg><span>(08) 9473 2257</span></li>
    <li><svg viewBox="0 0 20 20"><path d="M2 5h16v10H2z"/><path class="cut" d="M2 5l8 6 8-6" fill="none" stroke-width="1.2"/></svg><span>salvage@tkwreck.com.au</span></li>
    <li><svg viewBox="0 0 20 20"><circle cx="10" cy="10" r="8"/><path class="cut" d="M2 10h16M10 2v16" stroke-width="1.2"/></svg><span>tolvanekdemolition.com.au</span></li>
  </ul>
  <section class="hours">
    <h2 class="hours__title">Opening Hours:</h2>
    <p>Monday to Friday 8am - 5.00pm</p>
    <p>Saturday 8am - 3pm</p>
    <p>Closed Sunday's and public holidays</p>
  </section>
</article>

<article class="card card--dark">
  <div class="brand-mark"><span class="brand-mark__dot"></span><span class="brand-mark__name">Tolvanek</span></div>
  <h1 class="company"><span>Tolvanek Demolition</span><span>&amp; Salvage (WA) Pty Ltd</span></h1>
  <ul class="contacts">
    <li><svg viewBox="0 0 20 20"><path d="M10 1a6 6 0 0 0-6 6c0 5 6 12 6 12s6-7 6-12a6 6 0 0 0-6-6z"/></svg><span>2317 Carrowby Ridge Road<br>LOWER MIRRABEL WA 6182</span></li>
    <li><svg viewBox="0 0 20 20"><path d="M5 2l3 4-2 2c1 2 3 4 5 5l2-2 4 3-2 4C8 17 3 12 2 5z"/></svg><span>(08) 9473 5068</span></li>
    <li><svg viewBox="0 0 20 20"><path d="M5 2h8v5H5zM2 8h16v8H2zM5 13h10v5H5z"/></svg><span>(08) 9473 2257</span></li>
    <li><svg viewBox="0 0 20 20"><path d="M2 5h16v10H2z"/><path class="cut" d="M2 5l8 6 8-6" fill="none" stroke-width="1.2"/></svg><span>salvage@tkwreck.com.au</span></li>
    <li><svg viewBox="0 0 20 20"><circle cx="10" cy="10" r="8"/><path class="cut" d="M2 10h16M10 2v16" stroke-width="1.2"/></svg><span>tolvanekdemolition.com.au</span></li>
  </ul>
  <section class="hours">
    <h2 class="hours__title">Opening Hours:</h2>
    <p>Monday to Friday 8am - 5.00pm</p>
    <p>Saturday 8am - 3pm</p>
    <p>Closed Sunday's and public holidays</p>
  </section>
</article>

</body>
</html>
```